Lantern - Web Design Project

We are seeking to have our website redesigned. Our current webpage is rather dated looking www.lantern-outcomes.com We will be utilizing similar content to explain our services as what is in the website now. We do not see it at a retail portal but rather a website for those inquiring about our services as a reference check so to speak.

We wish to have a look that is considered clean, fresh, contemporary and contains a business savvy vibe.

We prefer isolated white background and also wish to retain the integrity of our Logo and colour scheme.

We are looking for something that doesnt look like it was designed at home on sitemoose. We are hoping to find something that looks like it would reside on a tablet.
Updates

Hello designers!

We apologize for our tardiness as we have been quite preoccupied. We will be extending our invites to the end of January!

Hello All,

Please review our offer once again for updated requirements.  We are hoping to accept a design by months end.

Lantern

Target Market(s)

Business to business clients and Large manufacturers

Industry/Entity Type

Retail

Requirements
Must have
• Existing Logo

There must be an area dedicated to an intro video that will be incorporated on our landing page.

We require design of the other pages as well not only the landing page.

```html
<!DOCTYPE html>
<html lang="en">
<head>
<meta charset="utf-8">
<title>Lantern – Contact</title>
<link rel="stylesheet" href="https://fonts.googleapis.com/css2?family=Questrial&family=PT+Sans:wght@400;700&family=PT+Sans+Narrow:wght@700&display=swap">
<style>
  :root {
    --page-bg: #ffffff;
    --panel-bg: #e9e9e9;
    --field-bg: #ffffff;
    --accent: #6b1010;
    --ink: #1c1c1c;
    --placeholder: #9a9a9a;
    --nav-bg: #000000;
    --nav-text: #8c8c8c;
    --nav-divider: #2a2a2a;
    --nav-active: #8f6b6b;
    --logo: #4a4545;
    --road-light: #f4f4f4;
    --road-mid: #c9c9c9;
    --road-dark: #8d8d8d;
  }
  * { box-sizing: border-box; margin: 0; padding: 0; }
  html, body { width: 1200px; height: 966px; overflow: hidden; background: var(--page-bg); }
  body { position: relative; font-family: "PT Sans", sans-serif; color: var(--ink); }

  .hero-backdrop {
    position: absolute; left: 470px; top: 0; width: 730px; height: 840px;
    background:
      radial-gradient(ellipse at 85% 20%, var(--road-dark) 0%, var(--road-mid) 35%, rgba(255,255,255,0) 70%),
      linear-gradient(100deg, var(--page-bg) 10%, var(--road-light) 30%, var(--road-mid) 60%, var(--road-light) 95%);
  }

  .brand {
    position: absolute; left: 97px; top: 96px;
    display: flex; align-items: center; gap: 10px;
    font-family: "Questrial", sans-serif; font-size: 50px; color: var(--logo);
  }
  .brand-dot { width: 16px; height: 16px; border-radius: 50%; background: var(--accent); }

  .contact-panel {
    position: absolute; left: 42px; top: 256px; width: 1113px; height: 556px;
    background: var(--panel-bg);
  }
  .panel-close {
    position: absolute; right: 16px; top: 12px;
    font-size: 16px; color: var(--ink);
  }
  .panel-heading {
    position: absolute; top: 55px;
    font-family: "Questrial", sans-serif; font-size: 25px; font-weight: 400;
    color: var(--accent); letter-spacing: -0.3px;
  }
  .address-heading { left: 39px; }
  .contact-heading { left: 633px; }

  .map-frame {
    position: absolute; left: 39px; top: 107px; width: 506px; height: 255px;
    background: var(--field-bg); padding: 9px;
  }
  .map-area {
    width: 100%; height: 100%;
    background: linear-gradient(135deg, #e6e4de 0%, #dcdad3 55%, #b9cde3 75%, #dcdad3 90%);
  }

  .address-lines {
    position: absolute; left: 39px; top: 390px;
    font-family: "PT Sans Narrow", sans-serif; font-weight: 700;
    font-size: 21px; line-height: 24px; color: var(--accent); text-transform: uppercase;
  }
  .contact-lines {
    position: absolute; left: 39px; top: 455px;
    font-size: 14px; line-height: 22px;
  }
  .contact-lines .label { margin-right: 10px; }

  .contact-form { position: absolute; left: 633px; top: 107px; }
  .field {
    display: block; width: 242px; height: 36px; margin-bottom: 9px;
    background: var(--field-bg); border: none;
    padding: 0 15px; font-family: "PT Sans", sans-serif; font-size: 13px; color: var(--ink);
  }
  .field::placeholder { color: var(--placeholder); }
  .field-message { width: 440px; height: 225px; padding: 12px 15px; resize: none; }
  .form-actions {
    position: absolute; left: 0; top: 381px; width: 440px;
    display: flex; justify-content: flex-end; gap: 40px; padding-right: 17px;
  }
  .form-button {
    background: none; border: none; font-family: "Questrial", sans-serif;
    font-size: 13px; color: var(--ink); cursor: pointer;
  }

  .main-nav {
    position: absolute; left: 46px; top: 830px; width: 1108px; height: 116px;
    background: var(--nav-bg);
  }
  .nav-item {
    position: absolute; top: 21px; height: 73px;
    display: flex; align-items: center; justify-content: center;
    font-family: "Questrial", sans-serif; font-size: 19px; letter-spacing: -0.6px;
    color: var(--nav-text); text-decoration: none; text-transform: uppercase;
  }
  .nav-divider { position: absolute; top: 21px; width: 1px; height: 73px; background: var(--nav-divider); }
  .nav-item.is-active { background: var(--nav-active); color: #f2eded; }
</style>
</head>
<body>
  <div class="hero-backdrop" role="img" aria-label="Blurred photograph of a grey highway stretching into the distance"></div>

  <div class="brand"><span>Lantern</span><span class="brand-dot"></span></div>

  <section class="contact-panel">
    <span class="panel-close">×</span>

    <h2 class="panel-heading address-heading">ADDRESS</h2>
    <div class="map-frame">
      <div class="map-area" role="img" aria-label="Street map showing the office location with a marker"></div>
    </div>
    <p class="address-lines">58 Harrowgate Rd, Kingsford<br>ON K2B 4M7, Canada</p>
    <p class="contact-lines">
      <span class="label">Telephone:</span> +1.800.555.0142<br>
      <span>E-mail:</span> info@lantern-outcomes.com
    </p>

    <h2 class="panel-heading contact-heading">CONTACT US</h2>
    <form class="contact-form">
      <input class="field" type="text" placeholder="Your Name:">
      <input class="field" type="tel" placeholder="Telephone:">
      <input class="field" type="email" placeholder="E-mail:">
      <textarea class="field field-message" placeholder="Message:"></textarea>
      <div class="form-actions">
        <button class="form-button" type="reset">RESET</button>
        <button class="form-button" type="submit">SUBMIT</button>
      </div>
    </form>
  </section>

  <nav class="main-nav">
    <a class="nav-item" href="#" style="left:18px;width:98px;">Home</a>
    <span class="nav-divider" style="left:128px;"></span>
    <a class="nav-item" href="#" style="left:140px;width:158px;">Who we are</a>
    <span class="nav-divider" style="left:312px;"></span>
    <a class="nav-item" href="#" style="left:316px;width:294px;">Performance solutions</a>
    <span class="nav-divider" style="left:617px;"></span>
    <a class="nav-item" href="#" style="left:622px;width:232px;">Sustain solutions</a>
    <span class="nav-divider" style="left:860px;"></span>
    <a class="nav-item is-active" href="#" style="left:866px;width:225px;">Cross the Lantern</a>
  </nav>
</body>
</html>
```